Copper Heron Bar & Grill Takeout Menu

Please create a takeout menu using the attached dine-in menu.
Take out menu size: Tri-Fold 11x17

Industry/Entity Type

Bar & Grill (Restaurant)

Colors

Designer to choose colors to be used in the design.

Requirements
Must have
• Phone number and website. "Order Online" "Order for Delivery"
Nice to have
• Area on the back of the menu to feature happy hour specials.

```html
<!DOCTYPE html>
<html lang="en">
<head>
<meta charset="utf-8">
<title>Copper Heron Bar &amp; Grill – Takeout Menu</title>
<link rel="stylesheet" href="https://fonts.googleapis.com/css2?family=Cormorant+Garamond:ital,wght@0,700;1,600;1,700&family=Oswald:wght@400;500&family=Poppins:ital,wght@0,300;1,300&display=swap">
<style>
:root{
  --page:#e9e6e1;
  --board:#1d1d1d;
  --board-deep:#121212;
  --edge:#2b2b2b;
  --amber:#f6a21d;
  --chalk:#f4f1ea;
  --chalk-soft:#b9b6b0;
  --line:#e8e5de;
  --head:"Cormorant Garamond", Georgia, serif;
  --label:"Oswald", "Arial Narrow", sans-serif;
  --body:"Poppins", Arial, sans-serif;
}
*{margin:0;padding:0;box-sizing:border-box}
html,body{width:926px;height:1200px;overflow:hidden;background:var(--page)}
.canvas{position:relative;width:926px;height:1200px}
.sheet{position:absolute;left:27px;width:870px;background:radial-gradient(ellipse at 40% 35%,#2c2c2c 0%,var(--board) 55%,var(--board-deep) 100%);border:6px solid var(--edge)}
.sheet-outside{top:30px;height:566px}
.sheet-inside{top:608px;height:568px}
.a{position:absolute;white-space:nowrap}
.heading{font-family:var(--head);font-style:italic;font-weight:700;color:var(--amber);text-transform:uppercase;letter-spacing:.5px}
.subhead{font-family:var(--head);font-style:italic;font-weight:700;color:var(--amber);text-transform:uppercase}
.note{font-family:var(--head);font-style:italic;font-weight:600;color:var(--chalk);font-size:7.5px;line-height:9px}
.label{font-family:var(--label);font-weight:400;color:var(--chalk);text-transform:uppercase}
.name{font-family:var(--label);font-weight:500;color:var(--chalk);text-transform:uppercase;letter-spacing:.2px}
.desc{font-family:var(--body);font-style:italic;font-weight:300;color:var(--chalk-soft);font-size:4.4px;line-height:5.6px;white-space:normal}
.price{font-family:var(--label);font-weight:500;color:var(--amber)}
.price::before{content:"|";color:var(--amber);margin-right:3px;font-weight:300}
.price.plain::before{content:none}
.amber{color:var(--amber)}
.art{position:absolute;border-radius:6px}
.card{position:absolute;left:323px;top:40px;width:277px;height:544px;border:1.5px solid var(--line);border-radius:12px}
.cover{position:absolute;left:609px;top:40px;width:278px;height:544px;border:1.5px solid var(--line);border-radius:12px}
.special{position:absolute;left:363px;width:198px;border:1px solid #9c9a96;outline:1px solid #6d6b68;outline-offset:3px}
.day{font-family:var(--head);font-style:italic;font-weight:700;color:var(--chalk);font-size:24px;text-align:center;text-transform:uppercase;line-height:30px}
.deal{font-family:var(--label);color:var(--chalk);font-size:11px;text-align:center;line-height:18px}
.brand{font-family:var(--label);font-weight:500;color:var(--chalk);text-transform:uppercase}
.rule{position:absolute;height:1px;background:var(--line)}
.r{text-align:right}
.c{text-align:center}
</style>
</head>
<body>
<div class="canvas">

  <!-- OUTSIDE SHEET -->
  <div class="sheet sheet-outside"></div>

  <!-- background art for kids area sits beneath the text -->
  <div class="art" role="img" aria-label="Faint chalk sketch of a sitting cat" style="left:34px;top:412px;width:70px;height:170px;background:linear-gradient(160deg,rgba(255,255,255,.05),rgba(255,255,255,.01))"></div>
  <div class="art" role="img" aria-label="Grey long-haired cat holding a coffee cup" style="left:262px;top:498px;width:60px;height:86px;background:linear-gradient(180deg,rgba(70,70,70,.6),rgba(36,36,36,.8))"></div>

  <!-- Other handhelds panel -->
  <div class="a heading" style="left:40px;top:66px;font-size:23px">Other Handhelds:</div>
  <div class="a note" style="left:40px;top:98px">All served with Hand Cut Fries or Sweet Potato Fries.<br>Premium sides available for an up charge <b>+$2</b></div>

  <div class="a name" style="left:38px;top:137px;font-size:8px">Cat Club</div>
  <div class="a desc" style="left:38px;top:151px;width:130px">Sliced whole wheat bread with roasted garlic aioli, grilled marinated chicken breast, provolone cheese bacon, lettuce and tomato.</div>
  <div class="a price" style="left:184px;top:150px;font-size:10px">11</div>

  <div class="a name" style="left:40px;top:185px;font-size:8px">Southwest Melt</div>
  <div class="a desc" style="left:40px;top:198px;width:130px">Sliced whole wheat bread with roasted garlic aioli,3 pepper colby jack, roasted red peppers and corn.</div>
  <div class="a price" style="left:184px;top:195px;font-size:10px">11</div>

  <div class="a name" style="left:40px;top:230px;font-size:8px">What's Gouda?</div>
  <div class="a desc" style="left:40px;top:243px;width:130px">Sliced whole wheat bread with roasted garlic aioli smoked gouda and provolone cheeses, roasted red peppers and portobello mushrooms.</div>
  <div class="a price" style="left:184px;top:240px;font-size:10px">11</div>

  <div class="a name" style="left:40px;top:282px;font-size:8px">Westover Melt</div>
  <div class="a desc" style="left:40px;top:295px;width:130px">Sliced whole wheat bread with roasted garlic aioli, zucchini, portobello mushrooms, red peppers, with melted brie and provolone cheeses,</div>
  <div class="a price" style="left:184px;top:292px;font-size:10px">11</div>

  <div class="a subhead r" style="right:616px;top:159px;font-size:12px">Cheeses</div>
  <div class="a desc r" style="right:616px;top:176px;width:90px">Horseradish Aioli | Chipotle Crema | Roasted Garlic Aioli | Citrus Aioli Spicy Ketchup | Dijon Mustard | Yellow Mustard | Mayo | Ketchup</div>
  <div class="a subhead r" style="right:616px;top:204px;font-size:12px">Condiments</div>
  <div class="a desc r" style="right:616px;top:221px;width:90px">Horseradish Aioli | Chipotle Crema | Roasted Garlic Aioli | Citrus Aioli Spicy Ketchup | Dijon Mustard | Yellow Mustard | Mayo | Ketchup</div>
  <div class="a subhead r" style="right:616px;top:250px;font-size:12px">Toppings</div>
  <div class="a desc r" style="right:616px;top:267px;width:90px">Horseradish Aioli | Chipotle Crema | Roasted Garlic Aioli | Citrus Aioli Spicy Ketchup | Dijon Mustard | Yellow Mustard | Mayo | Ketchup</div>

  <div class="a subhead" style="left:38px;top:326px;font-size:13px">Sides:</div>
  <div class="a label r" style="right:636px;top:328px;font-size:7.5px">Fire Roasted Veggies</div>
  <div class="a price" style="left:296px;top:326px;font-size:10px">11</div>
  <div class="a label r" style="right:636px;top:346px;font-size:7.5px">Potato Salad</div>
  <div class="a price" style="left:296px;top:344px;font-size:10px">11</div>
  <div class="a label r" style="right:636px;top:366px;font-size:7.5px">Brown Rice, Quinoa, &amp; Kale Medley</div>
  <div class="a price" style="left:296px;top:364px;font-size:10px">11</div>

  <div class="a heading c" style="left:100px;top:398px;width:148px;font-size:24px">Kids Menu</div>
  <div class="a note c" style="left:100px;top:425px;width:148px;font-size:8px">All served with French Fries</div>
  <div class="a label" style="left:72px;top:463px;font-size:7.5px">Grilled Cheese</div>
  <div class="a price" style="left:150px;top:460px;font-size:10px">11</div>
  <div class="a label" style="left:186px;top:463px;font-size:7.5px">Mac &amp; Cheese</div>
  <div class="a price" style="left:255px;top:460px;font-size:10px">11</div>
  <div class="a label" style="left:72px;top:482px;font-size:7.5px">Cheese Quesadilla</div>
  <div class="a price" style="left:150px;top:479px;font-size:10px">11</div>
  <div class="a label" style="left:186px;top:482px;font-size:7.5px">Chicken Tenders</div>
  <div class="a price" style="left:255px;top:479px;font-size:10px">11</div>

  <!-- Happy hour panel -->
  <div class="card"></div>
  <div class="a brand c" style="left:323px;top:70px;width:277px;font-size:16px;line-height:20px">Copper Heron<br>Bar &amp; Grill</div>
  <div class="a heading c" style="left:323px;top:133px;width:277px;font-size:23px;text-transform:none">Happy Hour Specials</div>
  <div class="art" role="img" aria-label="Hand-drawn flourish divider" style="left:398px;top:178px;width:126px;height:12px;background:linear-gradient(90deg,transparent,rgba(244,241,234,.35),transparent)"></div>

  <div class="special" style="top:213px;height:84px">
    <div class="day" style="margin-top:9px">Wednesday</div>
    <div class="deal" style="margin-top:6px">$2.00 OFF WINE &amp; DRAFT BEER</div>
  </div>
  <div class="rule" style="left:371px;top:318px;width:176px"></div>
  <div class="special" style="top:338px;height:149px">
    <div class="day" style="margin-top:20px">Thursday<br>&amp; Friday</div>
    <div class="deal" style="margin-top:10px">$2.00 OFF WINE &amp; DRAFT BEER<br>$4.00 OFF COCKTAILS</div>
  </div>
  <div class="art" role="img" aria-label="Hand-drawn flourish ornament" style="left:370px;top:512px;width:182px;height:30px;background:linear-gradient(90deg,transparent,rgba(244,241,234,.3),transparent)"></div>

  <!-- Cover panel -->
  <div class="cover"></div>
  <svg class="a" style="left:682px;top:50px" width="18" height="18" viewBox="0 0 18 18" aria-hidden="true"><circle cx="9" cy="9" r="8" fill="#4a4a4a"/></svg>
  <div class="a note" style="left:711px;top:50px;font-size:12px;line-height:14px">1420 Linden Ave,<br>Fairview, VA 22031</div>
  <svg class="a" style="left:700px;top:135px" width="172" height="172" viewBox="0 0 172 172" aria-hidden="true"><circle cx="86" cy="86" r="85" fill="var(--amber)"/></svg>
  <div class="a brand" style="left:646px;top:160px;font-size:34px;line-height:40px">Copper<br>Heron</div>
  <div class="a brand" style="left:649px;top:302px;font-size:26px">Bar &amp; Grill</div>
  <div class="rule" style="left:668px;top:376px;width:16px"></div>
  <div class="a heading c" style="left:690px;top:354px;width:116px;font-size:34px;color:var(--chalk)">Menu</div>
  <div class="rule" style="left:800px;top:376px;width:16px"></div>
  <div class="a label c" style="left:609px;top:491px;width:278px;font-size:16px;font-weight:500">Order Delivery</div>
  <div class="a label c" style="left:609px;top:512px;width:278px;font-size:16px;font-weight:500">▪&nbsp; www.copperherongrill.com &nbsp;▪</div>
  <div class="a label c" style="left:609px;top:535px;width:278px;font-size:16px;font-weight:500">
    <svg width="15" height="15" viewBox="0 0 24 24" style="vertical-align:-2px" aria-hidden="true"><path d="M6.6 10.8a15 15 0 0 0 6.6 6.6l2.2-2.2a1 1 0 0 1 1-.25 11.4 11.4 0 0 0 3.6.6 1 1 0 0 1 1 1V20a1 1 0 0 1-1 1A17 17 0 0 1 3 4a1 1 0 0 1 1-1h3.5a1 1 0 0 1 1 1c0 1.25.2 2.45.6 3.6a1 1 0 0 1-.25 1z" fill="none" stroke="currentColor" stroke-width="2"/></svg>
    555 014 7720</div>

  <!-- INSIDE SHEET -->
  <div class="sheet sheet-inside"></div>

  <!-- Salads -->
  <div class="a heading" style="left:42px;top:632px;font-size:23px">Salads</div>
  <div class="a heading" style="left:288px;top:634px;font-size:16px">$</div>

  <div class="a name" style="left:41px;top:677px;font-size:16px">Combo Cat</div>
  <div class="a desc" style="left:41px;top:697px;width:150px">Enjoy a side House and a cup of any soup.</div>
  <div class="a price" style="left:283px;top:681px;font-size:10px">11</div>

  <div class="a name" style="left:41px;top:716px;font-size:16px">Cat House Salad</div>
  <div class="a desc" style="left:41px;top:736px;width:110px">Spring lettuce mix, fresh red peppers, onion, cherry tomatoes, cucumber, and croutons. Served with Red Wine Vinaigrette.</div>
  <div class="a price" style="left:283px;top:720px;font-size:10px">11</div>

  <div class="a name" style="left:41px;top:760px;font-size:16px">Grilled Chicken Salad</div>
  <div class="a desc" style="left:41px;top:782px;width:110px">Spring lettuce mix, grilled chicken breast, bacon, fresh red peppers, onions, tomatoes, cucumber and feta cheese. Served with Red Wine Vinaigrette</div>
  <div class="a price" style="left:283px;top:764px;font-size:10px">15</div>

  <div class="a name" style="left:41px;top:813px;font-size:16px">Grilled Shrimp Salad<span class="amber">*</span></div>
  <div class="a desc" style="left:41px;top:839px;width:180px">Spring lettuce mix, garlic Roasted Shrimp, roasted corn, pico de gallo fresh avocado, Served with Lemon Champagne Vinaigrette</div>
  <div class="a price" style="left:283px;top:817px;font-size:10px">16</div>

  <div class="a name" style="left:41px;top:868px;font-size:16px">Goat Cheese Salad</div>
  <div class="a desc" style="left:41px;top:890px;width:150px">Spring lettuce mix, fried goat cheese, fresh red peppers, cranberries, white onions, and cherry tomatoes. Served with Lemon Champagne Vinaigrette.</div>
  <div class="a price" style="left:283px;top:872px;font-size:10px">16</div>

  <div class="a name" style="left:41px;top:918px;font-size:16px">The Skinny Cat</div>
  <div class="a desc" style="left:41px;top:940px;width:150px">Spring lettuce mix, sliced apple, sun dried cranberries, roasted corn, cherry tomatoes, and feta cheese. Served with Balsamic Vinaigrette.</div>
  <div class="a price" style="left:283px;top:922px;font-size:10px">14</div>

  <div class="a name" style="left:41px;top:974px;font-size:16px">Small House Salad</div>
  <div class="a price" style="left:283px;top:978px;font-size:10px">16</div>

  <div class="a note" style="left:47px;top:1015px;font-size:11px">Add:</div>
  <div class="a label" style="left:95px;top:1015px;font-size:8px;line-height:15px">Grilled Chicken <span class="amber">5</span> | Garlic Roasted Shrimp <span class="amber">5</span><br>Fried Goat Cheese <span class="amber">4</span></div>
  <div class="a note" style="left:47px;top:1050px;font-size:11px">Dressings</div>
  <div class="a label" style="left:95px;top:1050px;font-size:8.5px;line-height:14.5px">Balsamic Vinaigrette | Caesar<br>Red Wine Vinaigrette | Honey-Mustard | Lemon<br>Champagne Vinaigrette | Ranch | Blue Cheese</div>
  <div class="a note" style="left:112px;top:1106px;font-size:11px">Vegetarian &nbsp;&nbsp;&nbsp; spicy</div>
  <div class="a note" style="left:44px;top:1126px;font-size:7px;line-height:10px"><span class="amber">*</span> The consumption of raw or undercooked eggs, meat, poultry, seafood or shellfish<br>&nbsp;&nbsp;&nbsp;may contribute to food bornellness, especially if you have a medical condition.</div>

  <!-- Starters -->
  <div class="a heading c" style="left:324px;top:632px;width:254px;font-size:23px">Starters</div>

  <div class="a name" style="left:325px;top:677px;font-size:16px">Tortilla Chips:</div>
  <div class="a desc" style="left:325px;top:699px;width:110px">Flash-fried to a crispy golden brown and tossed in your choice of sauce. Choose from our Signature Hot, or Mild Sauce, or BBQ. Your choice of ranch or blue cheese.</div>
  <div class="a label r" style="right:347px;top:686px;font-size:7.5px">With House-made Salsa Verde</div>
  <div class="a price" style="left:585px;top:684px;font-size:10px">7</div>
  <div class="a label r" style="right:347px;top:700px;font-size:7.5px">With House-made Fire Roasted Salsa</div>
  <div class="a price" style="left:585px;top:698px;font-size:10px">7</div>
  <div class="a label r" style="right:347px;top:714px;font-size:7.5px">With Guacamole &amp; Pico de Gallo</div>
  <div class="a price" style="left:585px;top:712px;font-size:10px">8</div>
  <div class="a label r" style="right:347px;top:728px;font-size:7.5px">With Chili con Queso <span class="amber">| 8</span>&nbsp; With Queso</div>
  <div class="a price" style="left:585px;top:726px;font-size:10px">9</div>

  <div class="a name" style="left:325px;top:749px;font-size:16px">Quesadillas:</div>
  <div class="a desc" style="left:325px;top:772px;width:115px">All quesadillas are stuffed with roasted red peppers, black beans and your choice below. Served with guacamole, pico de gallo, and chipotle crema on the side.</div>
  <div class="a label r" style="right:347px;top:753px;font-size:7.5px">Cheddar and Monterey Jack Cheese</div>
  <div class="a price" style="left:585px;top:751px;font-size:10px">12</div>
  <div class="a label r" style="right:347px;top:767px;font-size:7.5px">Pulled Marinated Chicken &amp; Cheese</div>
  <div class="a price" style="left:585px;top:765px;font-size:10px">16</div>
  <div class="a label r" style="right:347px;top:781px;font-size:7.5px">Fire Roasted Vegetables &amp; Cheese</div>
  <div class="a price" style="left:585px;top:779px;font-size:10px">14</div>
  <div class="a label r" style="right:347px;top:795px;font-size:7.5px">Garlic Roasted Shrimp &amp; Cheese</div>
  <div class="a price" style="left:585px;top:793px;font-size:10px">16</div>

  <div class="a name" style="left:325px;top:811px;font-size:16px">Claw-full Nachos:</div>
  <div class="a desc" style="left:325px;top:834px;width:115px">All quesadillas are stuffed with roasted red peppers, black beans and your choice below. Served with guacamole, pico de gallo, and chipotle crema on the side.</div>
  <div class="a label r" style="right:347px;top:820px;font-size:7.5px">Copper Heron Chili Nachos</div>
  <div class="a price" style="left:585px;top:818px;font-size:10px">14</div>
  <div class="a label r" style="right:347px;top:834px;font-size:7.5px">Pulled Chicken Nachos</div>
  <div class="a price" style="left:585px;top:832px;font-size:10px">16</div>
  <div class="a label r" style="right:347px;top:848px;font-size:7.5px">Garlic Roasted Shrimp</div>
  <div class="a price" style="left:585px;top:846px;font-size:10px">16</div>
  <div class="a label r" style="right:347px;top:862px;font-size:7.5px">Fire Roasted Vegetables Nachos</div>
  <div class="a price" style="left:585px;top:860px;font-size:10px">14</div>

  <div class="a name" style="left:325px;top:880px;font-size:16px">French Fries:</div>
  <div class="a desc" style="left:325px;top:903px;width:115px">Served with our house made Garlic Aioli and Spicy Ketchup<br>Topped with Copper Heron Chili, cheddar jack cheese and served with chipotle crema on the side. <span class="amber">*</span></div>
  <div class="a label r" style="right:347px;top:889px;font-size:7.5px">Fries Only</div>
  <div class="a price" style="left:585px;top:887px;font-size:10px">7</div>
  <div class="a label r" style="right:347px;top:903px;font-size:7.5px">Sweet Potato Fries</div>
  <div class="a price" style="left:585px;top:901px;font-size:10px">7</div>
  <div class="a label r" style="right:347px;top:917px;font-size:7.5px">Cheddar-Jack Cheese Fries</div>
  <div class="a price" style="left:585px;top:915px;font-size:10px">8</div>
  <div class="a label r" style="right:347px;top:931px;font-size:7.5px">Cheddar-Jack Cheese, Bacon Fries</div>
  <div class="a price" style="left:585px;top:929px;font-size:10px">9</div>
  <div class="a label r" style="right:347px;top:945px;font-size:7.5px"><span class="amber">*</span>&nbsp; Chili Cheese Fries</div>
  <div class="a price" style="left:585px;top:943px;font-size:10px">10</div>

  <div class="a name" style="left:327px;top:957px;font-size:16px">Wings:</div>
  <div class="a desc" style="left:327px;top:980px;width:115px">Flash-fried to a crispy golden brown and tossed in your choice of sauce. Choose from our Signature Hot, or Mild Sauce, or BBQ. Your choice of ranch or blue cheese.</div>
  <div class="a label r" style="right:347px;top:971px;font-size:7.5px">8 Pieces</div>
  <div class="a price" style="left:585px;top:969px;font-size:10px">14</div>

  <div class="a heading" style="left:324px;top:1010px;font-size:23px">Soups &amp; Bowls</div>
  <div class="a label" style="left:325px;top:1044px;font-size:8px">Copper Heron Chili <span class="amber">| Cup 6 | </span>Bowl <span class="amber">8</span></div>
  <div class="a desc" style="left:325px;top:1058px;width:115px">Copper Heron Signature Chili with lean ground beef, black beans, and corn. Topped with cheddar cheese and green onion, served with tri-color tortilla chips.</div>
  <div class="a label" style="left:498px;top:1044px;font-size:8px;line-height:11px">Southwestern Sweet<br>Potato Soup .. Cup <span class="amber">6</span> | Bowl <span class="amber">8</span></div>
  <div class="a desc r" style="left:490px;top:1069px;width:110px">A delicious mix of sweet potatoes, corn, bell peppers, and black beans, this vegan soup delivers top flavor and quality with every bowl. Served with tri-color tortilla chips.</div>
  <div class="a label" style="left:325px;top:1084px;font-size:8px">Ancient Grains Bowl. | <span class="amber" style="font-size:10px">12</span></div>
  <div class="a desc" style="left:325px;top:1098px;width:115px">Quinoa, brown rice, kale and fresh spinach, with fire roasted portobello mushrooms, zucchini and red peppers. Topped with fresh avocado, and feta cheese. Served with Lemon Champagne Vinaigrette</div>
  <div class="a label r" style="right:327px;top:1093px;font-size:7.5px">Add: Grilled Chicken | <span class="amber">5</span></div>
  <div class="a label r" style="right:327px;top:1106px;font-size:7.5px">Garlic Roasted Shrimp | <span class="amber">5</span></div>

  <!-- Burgers -->
  <div class="a heading r" style="right:44px;top:634px;font-size:23px;line-height:30px">Gourmet Burgers<br>&amp; Sandwiches</div>
  <div class="a note" style="left:636px;top:692px;width:250px;white-space:normal;text-align:right;font-size:7.3px;line-height:10px">Start with your style and then choose your protein. Our burgers are house made and cooked to your temperature. Our Fresh grilled chicken breast is marinated in house and cooked to perfection. Keep it vegetarian by choosing a vegetarian style along with the Quinoa Lentil Burger. All are served on a potato bun with lettuce, tomato, onion, and your choice of hand cut fries or sweet potato fries.</div>
  <div class="a note amber r" style="right:42px;top:742px;font-size:9px">Premium sides available for an up charge + $2</div>

  <div class="a label" style="left:611px;top:787px;font-size:7px;line-height:10px">Gluten-free bun available<br>upon request | <span class="amber">$2</span></div>
  <svg class="a" style="left:771px;top:787px" width="100" height="16" viewBox="0 0 100 16" role="img" aria-label="Beef, chicken and vegetarian icons">
    <circle cx="7" cy="8" r="6" fill="none" stroke="var(--amber)" stroke-width="1.5"/>
    <circle cx="50" cy="8" r="6" fill="none" stroke="var(--amber)" stroke-width="1.5"/>
    <circle cx="93" cy="8" r="6" fill="none" stroke="var(--amber)" stroke-width="1"/>
  </svg>

  <div class="a name" style="left:611px;top:815px;font-size:16px">Calico Cat</div>
  <div class="a desc" style="left:611px;top:835px;width:100px">Roasted red peppers, red onions, brie cheese, and horseradish aioli.</div>
  <div class="a price plain" style="left:767px;top:828px;font-size:10px;word-spacing:13px">15.00 14.00 13.00</div>

  <div class="a name" style="left:611px;top:856px;font-size:16px">Tiger Cat</div>
  <div class="a desc" style="left:611px;top:876px;width:120px">Cheddar, Monterey Jack, and Provolone</div>
  <div class="a price plain" style="left:767px;top:860px;font-size:10px;word-spacing:13px">15.00 14.00 13.00</div>

  <div class="a name" style="left:611px;top:888px;font-size:16px">Cat Scratch Fever</div>
  <div class="a desc" style="left:611px;top:908px;width:130px">Guacamole, 3 pepper colby jack, pico de gallo, and chipotle mayo.</div>
  <div class="a price plain" style="left:767px;top:900px;font-size:10px;word-spacing:12px">15.50* 14.50 13.50</div>

  <div class="a name" style="left:611px;top:922px;font-size:16px">The Fat Cat</div>
  <div class="a desc" style="left:611px;top:943px;width:140px">Fried egg<span class="amber">*</span>, bacon, cheddar cheese, and garlic aioli.</div>
  <div class="a price plain" style="left:767px;top:930px;font-size:10px;word-spacing:12px">16.00* 15.00 14.00</div>

  <div class="a name" style="left:611px;top:955px;font-size:16px">Tabby Cat</div>
  <div class="a desc" style="left:611px;top:975px;width:140px">Melted brie cheese, sliced apple, and citrus aioli.</div>
  <div class="a price plain" style="left:767px;top:959px;font-size:10px;word-spacing:13px">16.50 15.50 14.50</div>

  <div class="a name" style="left:611px;top:984px;font-size:16px">The Sphynx</div>
  <div class="a desc" style="left:611px;top:1004px;width:150px">Portobello mushrooms, roasted red peppers, smoked gouda cheese, and roasted garlic aioli.</div>
  <div class="a price plain" style="left:767px;top:988px;font-size:10px;word-spacing:13px">16.50 15.50 14.50</div>

  <div class="a name" style="left:611px;top:1020px;font-size:16px">Maine Coon</div>
  <div class="a desc" style="left:611px;top:1040px;width:150px">Grilled shrimp<span class="amber">*</span>, roasted corn, swiss cheese, and roasted garlic aioli.</div>
  <div class="a price plain" style="left:767px;top:1025px;font-size:10px;word-spacing:13px">16.50 15.50 14.50</div>

  <div class="a name" style="left:611px;top:1057px;font-size:16px">Alley Cat</div>
  <div class="a desc" style="left:611px;top:1077px;width:150px">Whats up your alley? Choose a cheese, condiment and one topping :</div>
  <div class="a price plain" style="left:767px;top:1061px;font-size:10px;word-spacing:13px">14.00 13.00 12.00</div>

  <div class="a label" style="left:612px;top:1092px;font-size:7.5px">Additional Toppings | <span class="amber" style="font-size:9px">1</span></div>
  <div class="a label" style="left:612px;top:1105px;font-size:7.5px">Bacon, Egg, Shrimp &nbsp;&nbsp;&nbsp;| <span class="amber" style="font-size:9px">2</span></div>

</div>
</body>
</html>
```